Berrocal Tizón Law Firm for Small and Medium Business: Website

We need a web design that includes coding for the Wix platform, for a new company based in Santiago, Chile, called Berrocal Tizón, Abogados y Consultores. The company is essentially a law firm, with additional advisory services in accounting, tax management and finance. The main target of the company are founders, CEOs or C-level executives of small or medium companies based in Chile.
The main menu of the web page must have the following tab options:
- Home - About us - Services – How we work -Blog – FAQ -Contact
Our main services are:

1.- Commercial and corporate law advisory
2.- Legal defense in civil, criminal, labor and family matters (litigation and arbitration)
3.- Bankruptcy and reorganization of companies
4.- Collection and recovery of assets
5.- Asset protection
6.- Financial and tax advice

We want to highlight the following services:

-Bankruptcy and reorganization of companies
-Judicial defense in civil matters
-Financial and tax advice

In addition to these services, the following will be offered:
-Lawyer at your home for special cases
-Half hour free consultation
-Monthly service packages

The final design should communicate confidence, business savvy and high execution standards and quality.

Target Market(s)

The main target of the company are founders, CEOs or C-level executives of small or medium companies based in Chile.

Industry/Entity Type

Legal industry

Coding

Number of Pages Required

5+ page

Font styles to use
Serif

Requirements
Must have
• 1. Big banners para destacar los siguientes servicios: -Bankruptcy and reorganization of companies -Judicial defense in civil matters -Financial and tax advice 2. Call to action para agendar consulta legal. 3. Destacar los siguientes servicios: -Lawyer at your home for special cases -Half hour free consultation -Monthly service packages 3. Página para explicar cómo se cobra (precios transparentes): ver el siguiente sitio web: https://www.brookvanelegal.example/how 4. Links to Facebook, Instagram and Linkedin 5. Connection to Whatsapp.
Should not have
• Look old fashioned

```html
<!DOCTYPE html>
<html lang="en">
<head>
<meta charset="utf-8">
<title>Berrocal Tizón, Abogados y Consultores</title>
<link href="https://fonts.googleapis.com/css2?family=Poppins:wght@400;500;600&family=Questrial&display=swap" rel="stylesheet">
<style>
:root{
  --green:#163028;
  --green-deep:#10241e;
  --gold:#c9a82c;
  --gold-light:#e8d36a;
  --grey:#f2f2f2;
  --ink:#222;
  --muted:#666;
  --white:#fff;
}
*{margin:0;padding:0;box-sizing:border-box}
html,body{width:1200px;height:4209px;overflow:hidden}
body{position:relative;font-family:"Poppins",sans-serif;color:var(--ink);background:var(--white)}
.abs{position:absolute}
.heading{font-family:"Questrial",sans-serif;font-weight:400}
.rule{position:absolute;height:2px;width:44px;background:var(--gold)}

/* hero */
.hero{position:absolute;left:0;top:0;width:1200px;height:800px;background:var(--green)}
.hero-photo{position:absolute;left:560px;top:0;width:640px;height:800px;background:linear-gradient(100deg,rgba(22,48,40,0) 0%,rgba(14,32,27,.9) 35%,rgba(20,44,37,.7) 70%,rgba(22,48,40,0) 100%)}
.brand{position:absolute;display:flex;align-items:center;gap:8px;color:var(--gold);font-family:"Questrial",sans-serif}
.brand-mark{width:40px;height:40px;border:2px solid var(--gold)}
.brand-name{font-size:27px;line-height:1}
.brand-sub{font-size:8px;letter-spacing:1px;margin-top:3px;text-align:center}
.nav{position:absolute;top:31px;left:523px;display:flex;align-items:center;color:var(--white);font-size:15px;font-weight:500}
.nav a{color:inherit;text-decoration:none;position:absolute;white-space:nowrap;top:5px}
.nav .contact{top:0;border:2px solid var(--gold);width:113px;height:31px;text-align:center;line-height:27px}
.hero-frame{position:absolute;left:96px;top:219px;width:267px;height:389px;border:3px solid var(--gold)}
.hero-kicker{position:absolute;left:136px;top:296px;color:var(--white);font-size:15px}
.hero-title{position:absolute;left:136px;top:316px;color:var(--white);font-size:57px;line-height:63px;width:600px}
.hero-text{position:absolute;left:138px;top:455px;width:470px;color:var(--white);font-size:13.5px;line-height:24px}
.hero-link{position:absolute;left:138px;top:512px;color:var(--gold);font-size:13.5px;font-weight:500}
.dots{position:absolute;top:606px;left:1009px;display:flex;gap:12px}
.dots span{width:24px;height:4px;background:var(--white)}
.dots span.on{background:var(--gold)}
.hero-divider{position:absolute;left:95px;top:664px;width:1010px;height:1px;background:rgba(255,255,255,.12)}
.feature{position:absolute;top:700px;display:flex;align-items:center;gap:14px;color:var(--white);font-size:19px;line-height:24px;font-family:"Questrial",sans-serif}

/* welcome */
.band-grey{position:absolute;left:0;top:1339px;width:1200px;height:564px;background:var(--grey)}
.welcome-photo{position:absolute;left:162px;top:901px;width:437px;height:438px;background:linear-gradient(135deg,#5b4a3a,#2b2620 55%,#8a7f72)}
.welcome-card{position:absolute;left:602px;top:950px;width:435px;height:440px;background:var(--white);box-shadow:0 4px 30px rgba(0,0,0,.08)}
.card-title{position:absolute;left:659px;top:1021px;font-size:34px;line-height:43px;color:var(--ink)}
.body-text{font-size:15px;line-height:24.5px;color:var(--muted)}
.btn-outline{position:absolute;border:2px solid var(--gold);font-size:14px;font-weight:600;text-align:center;text-decoration:none;color:var(--ink)}

/* services */
.section-title{position:absolute;left:0;width:1200px;text-align:center;font-size:35px;color:var(--ink)}
.service{position:absolute;top:1542px;width:328px;height:258px;background:var(--white);box-shadow:0 3px 20px rgba(0,0,0,.05);text-align:center;font-family:"Questrial",sans-serif;font-size:20px;line-height:25px;color:#333}
.service.active{background:var(--green);color:var(--white)}
.service svg{position:absolute;left:122px;top:50px}
.service p{position:absolute;left:0;right:0;top:155px}

/* how we work */
.how{position:absolute;left:0;top:1903px;width:1200px;height:523px;background:linear-gradient(90deg,#15302a 0%,#1f3f38 45%,#4b5d5e 65%,#8d8f8c 100%)}
.how-title{position:absolute;left:93px;top:2068px;color:var(--white);font-size:35px}
.how-text{position:absolute;left:93px;top:2127px;width:400px;color:var(--white);font-size:15px;line-height:24.5px}
.how .btn-outline{color:var(--white)}

/* blogs */
.blog{position:absolute;top:2586px;width:328px;height:416px;background:var(--white);box-shadow:0 3px 20px rgba(0,0,0,.07)}
.blog-img{height:207px}
.blog-body{padding:24px 37px 0}
.blog-title{font-family:"Questrial",sans-serif;font-size:18.5px;line-height:25px;color:#333}
.blog-meta{display:flex;gap:14px;align-items:center;font-size:11.5px;color:#555;margin:6px 0 10px}
.blog-meta span{display:flex;align-items:center;gap:5px}
.blog-text{font-size:12.5px;line-height:21px;color:var(--muted)}
.blog-more{font-size:13.5px;color:var(--gold);margin-top:4px;font-weight:500}

/* faq */
.faq{position:absolute;left:250px;top:3170px;width:698px}
.faq-item{border-bottom:1px solid #ddd;position:relative;font-family:"Questrial",sans-serif;font-size:17.5px;color:#333;padding:12px 20px 14px 20px}
.faq-item .sign{position:absolute;right:22px;top:10px;font-size:20px;font-family:"Poppins",sans-serif;font-weight:600}
.faq-answer{font-family:"Poppins",sans-serif;font-size:14.5px;line-height:24.5px;color:var(--muted);margin-top:8px;padding-bottom:20px}

/* newsletter & footer */
.footer{position:absolute;left:0;top:3682px;width:1200px;height:527px;background:var(--green)}
.newsletter{position:absolute;left:95px;top:3574px;width:1010px;height:190px;background:linear-gradient(90deg,#b9962a 0%,#e5d265 40%,#d8bd4b 70%,#a88b2c 100%)}
.newsletter-art{position:absolute;right:0;top:0;width:360px;height:190px;background:linear-gradient(90deg,rgba(180,150,50,0),rgba(140,110,40,.45))}
.newsletter h2{position:absolute;left:52px;top:50px;font-size:37px;color:var(--green)}
.news-input{position:absolute;left:52px;top:98px;width:406px;height:39px;background:var(--white);font-size:13px;color:#555;padding:11px 20px}
.news-btn{position:absolute;left:458px;top:98px;width:134px;height:39px;background:var(--green);color:var(--white);font-size:12.5px;text-align:center;line-height:39px}
.foot-col{position:absolute;top:3890px;color:var(--white)}
.foot-col h3{font-family:"Questrial",sans-serif;font-weight:400;font-size:20px;margin-bottom:6px}
.foot-col li{list-style:none;font-size:13px;line-height:24.5px}
.socials{position:absolute;left:157px;top:4014px;display:flex;gap:11px}
.socials span{width:22px;height:22px;border-radius:50%;background:#2a473f;border:1px solid #3b5b52}
.foot-rule{position:absolute;left:95px;top:4148px;width:1010px;height:1px;background:rgba(255,255,255,.15)}
.foot-bottom{position:absolute;top:4170px;color:var(--white);font-size:16.5px}
.to-top{position:absolute;left:1117px;top:4126px;width:40px;height:40px;border-radius:50%;background:var(--gold);color:var(--green);text-align:center;line-height:38px;font-size:16px}
</style>
</head>
<body>

<!-- hero -->
<section class="hero">
  <div class="hero-photo" role="img" aria-label="Photo of a dark modern office tower"></div>
  <div class="brand" style="left:95px;top:20px">
    <div class="brand-mark"></div>
    <div><div class="brand-name">Berrocal Tizón</div><div class="brand-sub">ABOGADOS Y CONSULTORES</div></div>
  </div>
  <nav class="nav">
    <a style="left:0">About us</a>
    <a style="left:105px">Services</a>
    <a style="left:204px">How we work</a>
    <a style="left:342px">Blog</a>
    <a style="left:411px">FAQ</a>
    <a class="contact" style="left:469px">Contact</a>
  </nav>
  <div class="hero-frame"></div>
  <div class="hero-kicker">BERROCAL TIZÓN</div>
  <h1 class="hero-title heading">The company is essentially a law firm</h1>
  <p class="hero-text">Lorem Ipsum is simply dummy text of the printing and typesetting has been the industry's standard dummy .</p>
  <div class="hero-link">LEARN MORE</div>
  <div class="dots"><span></span><span class="on"></span><span></span></div>
  <div class="hero-divider"></div>

  <div class="feature" style="left:95px">
    <svg width="58" height="62" viewBox="0 0 58 62" fill="none" stroke="#c9a82c" stroke-width="2"><rect x="3" y="6" width="22" height="14" rx="2"/><circle cx="40" cy="13" r="9"/><path d="M37 10h5M37 16h5M40 8v10"/><path d="M12 20l14 22M20 58V40h8v18M32 58V34h8v24M44 58V44h8v14M8 58h48"/></svg>
    <div>Bankruptcy and<br>reorganization of companies</div>
  </div>
  <div class="feature" style="left:531px">
    <svg width="68" height="62" viewBox="0 0 68 62" fill="none" stroke="#c9a82c" stroke-width="2"><path d="M22 4l16 16M14 12l16 16M18 8l12 12-6 6-12-12z"/><path d="M27 23L4 46"/><rect x="26" y="48" width="36" height="6"/><rect x="22" y="54" width="44" height="6"/></svg>
    <div>Judicial defense in<br>civil matters</div>
  </div>
  <div class="feature" style="left:883px">
    <svg width="56" height="62" viewBox="0 0 56 62" fill="none" stroke="#c9a82c" stroke-width="2"><circle cx="32" cy="22" r="12"/><path d="M32 14v16M28 18h7a3 3 0 010 6h-6a3 3 0 000 6h7"/><path d="M4 40c8-4 14-2 20 2h12c3 0 3 5 0 5H24M4 52c10-4 20 2 28 0l18-10"/></svg>
    <div>Financial and<br>tax advice</div>
  </div>
</section>

<!-- welcome -->
<div class="band-grey"></div>
<div class="welcome-photo" role="img" aria-label="Photo of two lawyers in suits seated at a hearing"></div>
<div class="welcome-card"></div>
<h2 class="card-title heading">Welcome to the<br>Berrocal Tizón</h2>
<div class="rule" style="left:659px;top:1111px"></div>
<p class="body-text abs" style="left:660px;top:1126px;width:330px">Lorem Ipsum is simply dummy text of the printing and typesetting industry. Lorem Ipsum has been the industry's standard dummy text ever since the 1500s, when an unknown printer took a galley of type and scrambled it to make.</p>
<a class="btn-outline" style="left:664px;top:1285px;width:129px;height:34px;line-height:30px">READ MORE</a>

<!-- services -->
<h2 class="section-title heading" style="top:1470px">Our Services</h2>
<div class="rule" style="left:578px;top:1518px"></div>
<div class="service" style="left:93px">
  <svg width="84" height="84" viewBox="0 0 84 84" fill="none" stroke="#1d1d1d" stroke-width="2.2"><path d="M42 6v30M14 14h56M22 14l-10 22h20zM62 14l-10 22h20zM10 36a12 6 0 0024 0M50 36a12 6 0 0024 0"/><path d="M18 80V58l24-16 24 16v22zM34 80V64h16v16M10 80h64"/></svg>
  <p>Lawyer at your home<br>for special cases</p>
</div>
<div class="service active" style="left:435px">
  <svg width="84" height="84" viewBox="0 0 84 84" fill="none" stroke="#c9a82c" stroke-width="2.2"><circle cx="22" cy="14" r="8"/><path d="M10 40c0-10 6-16 12-16s12 6 12 16"/><rect x="6" y="40" width="44" height="8"/><path d="M10 48v30M46 48v30"/><circle cx="62" cy="18" r="8"/><path d="M52 78V40c0-8 5-12 10-12s10 4 10 12v38"/></svg>
  <p>Half hour free<br>consultation</p>
</div>
<div class="service" style="left:777px">
  <svg width="84" height="84" viewBox="0 0 84 84" fill="none" stroke="#1d1d1d" stroke-width="2.2"><path d="M12 36l30-12 30 12-30 12zM12 36v30l30 12 30-12V36M42 48v30M12 36l-8 10 30 12 8-10M72 36l8 10-30 12-8-10"/><circle cx="42" cy="20" r="8"/><path d="M42 6v4M42 30v4M28 20h4M52 20h4"/></svg>
  <p>Monthly service<br>packages</p>
</div>

<!-- how we work -->
<section class="how" role="img" aria-label="Photo of a thoughtful businessman with glasses at a laptop in an office">
</section>
<h2 class="how-title heading">How we work</h2>
<div class="rule" style="left:93px;top:2113px"></div>
<p class="how-text">Lorem Ipsum is simply dummy text of the printing and typesetting industry. Lorem Ipsum has been the industry's standard dummy text ever since the 1500s, when an unknown printer took a galley of type and scrambled it to make.</p>
<a class="btn-outline" style="left:95px;top:2260px;width:129px;height:34px;line-height:30px;color:#fff">READ MORE</a>

<!-- blogs -->
<h2 class="section-title heading" style="top:2515px">Our Latest Blogs</h2>
<div class="rule" style="left:578px;top:2564px"></div>

<article class="blog" style="left:93px">
  <div class="blog-img" role="img" aria-label="Photo of glass skyscrapers against a blue sky" style="background:linear-gradient(160deg,#8fb3d9,#2c4f7a 60%,#1a2c44)"></div>
  <div class="blog-body">
    <div class="blog-title">One problem of criminal activities is accounting</div>
    <div class="blog-meta"><span>▣ Feb 2020</span><span>○ Marta Ríos</span></div>
    <div class="blog-text">Lorem Ipsum is simply dummy text of the printing and typesetting industry.</div>
    <div class="blog-more">READ MORE</div>
  </div>
</article>
<article class="blog" style="left:435px">
  <div class="blog-img" role="img" aria-label="Photo of a businesswoman walking past stone columns" style="background:linear-gradient(90deg,#9a9a98,#d6d4cf 50%,#8d8c88)"></div>
  <div class="blog-body">
    <div class="blog-title">One problem of criminal activities is accounting</div>
    <div class="blog-meta"><span>▣ Feb 2020</span><span>○ Marta Ríos</span></div>
    <div class="blog-text">Lorem Ipsum is simply dummy text of the printing and typesetting industry.</div>
    <div class="blog-more">READ MORE</div>
  </div>
</article>
<article class="blog" style="left:777px">
  <div class="blog-img" role="img" aria-label="Photo of brass scales of justice on a desk" style="background:linear-gradient(120deg,#f1ede6,#c9b89a 50%,#7a5a34)"></div>
  <div class="blog-body">
    <div class="blog-title">One problem of criminal activities is accounting</div>
    <div class="blog-meta"><span>▣ Feb 2020</span><span>○ Marta Ríos</span></div>
    <div class="blog-text">Lorem Ipsum is simply dummy text of the printing and typesetting industry.</div>
    <div class="blog-more">READ MORE</div>
  </div>
</article>

<!-- faq -->
<h2 class="section-title heading" style="top:3090px">Frequently Asked Question</h2>
<div class="rule" style="left:578px;top:3139px"></div>
<div class="faq">
  <div class="faq-item">Lorem Ipsum is simply dummy text of the printing and typesetting ?<span class="sign">+</span></div>
  <div class="faq-item">It is a long established fact that a reader will be distracted ?<span class="sign">+</span></div>
  <div class="faq-item">There are many variations of passages of Lorem Ipsum ?<span class="sign">+</span></div>
  <div class="faq-item" style="padding-top:18px">Lorem Ipsum comes from sections 1.10.32 ?<span class="sign" style="top:14px">–</span>
    <p class="faq-answer">Lorem Ipsum is simply dummy text of the printing and typesetting industry. Lorem Ipsum has been the industry's standard dummy text ever since the 1500s, when an unknown printer took a galley of type and scrambled it to make.</p>
  </div>
</div>

<!-- footer -->
<footer class="footer"></footer>
<div class="newsletter">
  <div class="newsletter-art" role="img" aria-label="Faint photo of a judge's gavel on law books"></div>
  <h2 class="heading">Subscribe Newsletter</h2>
  <div class="news-input">Enter your email address</div>
  <div class="news-btn">SUBSCRIBE</div>
</div>

<div class="brand" style="left:95px;top:3960px">
  <div class="brand-mark"></div>
  <div><div class="brand-name">Berrocal Tizón</div><div class="brand-sub">ABOGADOS Y CONSULTORES</div></div>
</div>
<div class="socials"><span></span><span></span><span></span><span></span></div>

<div class="foot-col" style="left:407px">
  <h3>Useful Links</h3>
  <ul><li>About us</li><li>Services</li><li>How we work</li><li>Blog</li><li>FAQ</li><li>Contact</li></ul>
</div>
<div class="foot-col" style="left:576px">
  <h3>Service Offerings</h3>
  <ul><li>Commercial and corporate law advisory</li><li>Legal defense in civil, criminal...</li><li>Bankruptcy and reorganization of companies</li><li>Collection and recovery of assets</li><li>Asset protection</li><li>Financial and tax advice</li></ul>
</div>
<div class="foot-col" style="left:919px">
  <h3>Head Office</h3>
  <ul><li>Torre Alameda, 450 Av. Apoquindo,</li><li>Santiago, RM 7550000</li><li>Email: contacto@berrocaltizon.example</li><li>Phone: +56 2 2345 6780</li><li>Fax: +56 2 2345 6781</li><li>Get Directions</li></ul>
</div>

<div class="foot-rule"></div>
<div class="foot-bottom" style="left:95px">© 2021 Berrocal Tizón. All rights reserved.</div>
<div class="foot-bottom" style="left:781px">Terms and Conditions &nbsp;|&nbsp; Privacy Policy</div>
<div class="to-top">⌃</div>

</body>
</html>
```